Rise As Captain Book Cover Design

Book Cover Design Brief
Book Title
Rise As Captain
Subtitle
The 10 Quiet Habits of Remarkable Command
Author
Orwen Dalquist
Overview
This book is about leadership that starts within.
Most leadership books focus on tactics or management strategies. This book focuses on the inner disciplines that create powerful leaders — mindset, integrity, focus, empathy, professionalism, honesty, and self-respect.
The tone of the book is bold, direct, confident, and transformational.
This is not a soft or corporate leadership book. It is a call to step up and become the leader you are capable of becoming.
The cover should feel:
• Powerful
• Professional
• Transformational
• Premium
• Memorable
Think best-selling leadership book, not a generic business book.
Target Audience
Business owners
Managers
Entrepreneurs
Team leaders
Professionals who want to grow as leaders
Most readers are ambitious professionals who want to level up their leadership and life.
Design Direction
The design should communicate:
Strength. Discipline. Leadership. Personal transformation.
Avoid cliché leadership visuals like:
• Handshakes
• Office buildings
• Corporate stock imagery
• Teams sitting around tables
The design should feel iconic, bold, and timeless.
Think about covers of successful leadership books such as:
Copper Rituals
Total Stewardship
Won't Break Now
Begin From Purpose
The 36 Rules of Sway
These covers are simple, powerful, and recognizable even at small sizes.
Typography
The title RISE AS CAPTAIN should be:
• Bold
• Strong
• Dominant on the cover
• Easy to read even at small sizes (important for Vellora thumbnails)
The subtitle should be clean and secondary to the title.
The overall typography should feel strong, modern, and premium.
Color Direction
Designers are free to explore colors, but the cover should feel strong and premium, not playful.
Colors that often work well for leadership books include:
Black
Gold
White
Deep blue
Dark red
High contrast and clarity are important.
Style
Preferred style:
• Clean
• Modern
• Minimal
• Strong contrast
Avoid clutter and overly busy designs.
The goal is to create a cover that feels powerful and professional at first glance.
Deliverables
Front cover design for a leadership book.
Final files should include:
• High resolution artwork
• Editable source files
• Print-ready version suitable for publishing
Goal of the Cover
When someone sees this book on Vellora or in a bookstore, they should immediately think:
“This looks like a serious leadership book.”
The design should feel like it belongs next to books by authors such as:
Marcus Thorley
Brandt Osgood
Peter Hollis
Nolan Fairbrook
A strong, confident cover that attracts leaders who want to grow and perform at a higher level.
Target Market(s)
Business Owners and High level managers
Look and feel
Each slider illustrates characteristics of the customer's brand and the style your logo design should communicate.

```html
<!DOCTYPE html>
<html lang="en">
<head>
<meta charset="utf-8">
<title>Rise As Captain — Front Cover</title>
<link rel="stylesheet" href="https://fonts.googleapis.com/css2?family=League+Spartan:wght@700&family=Montserrat:wght@400&display=swap">
<style>
  :root {
    --stage: #c8c6cb;
    --paper: #ffffff;
    --navy: #00163f;
    --ink: #0b1a3d;
    --pawn-red: #c40018;
    --pawn-deep: #8e0013;
    --shadow-pale: #eef0f0;
  }
  * { margin: 0; padding: 0; box-sizing: border-box; }
  html, body {
    width: 1200px;
    height: 562px;
    overflow: hidden;
    background: var(--stage);
  }
  .stage {
    position: relative;
    width: 1200px;
    height: 562px;
  }
  .cover {
    position: absolute;
    left: 446px;
    top: 41px;
    width: 309px;
    height: 480px;
    background: var(--paper);
    overflow: hidden;
  }
  .cover-art {
    position: absolute;
    inset: 0;
    width: 100%;
    height: 100%;
  }
  .title {
    position: absolute;
    left: 44px;
    top: 104px;
    font-family: "League Spartan", "Futura", sans-serif;
    font-weight: 700;
    color: var(--ink);
    line-height: 0.86;
  }
  .title-lead {
    display: block;
    font-size: 34px;
    letter-spacing: 0.5px;
  }
  .title-main {
    display: block;
    font-size: 55px;
    letter-spacing: 0.5px;
  }
  .author {
    position: absolute;
    left: 0;
    right: 0;
    top: 452px;
    text-align: center;
    font-family: "Montserrat", "Helvetica Neue", sans-serif;
    font-weight: 400;
    font-size: 8px;
    letter-spacing: 0.2px;
    color: var(--paper);
  }
</style>
</head>
<body>
  <main class="stage">
    <article class="cover">
      <svg class="cover-art" viewBox="0 0 309 480" aria-hidden="false">
        <defs>
          <linearGradient id="pawn-tone" x1="0" y1="0" x2="0" y2="1">
            <stop offset="0" stop-color="var(--pawn-red)"/>
            <stop offset="0.42" stop-color="var(--pawn-deep)"/>
            <stop offset="0.5" stop-color="var(--shadow-pale)"/>
            <stop offset="1" stop-color="var(--shadow-pale)"/>
          </linearGradient>
        </defs>
        <polygon class="lower-band" points="0,340 309,266 309,480 0,480" fill="var(--navy)"/>
        <rect class="pawn-illustration" x="124" y="219" width="126" height="213" rx="10"
              fill="url(#pawn-tone)" role="img"
              aria-label="Illustration: a red chess pawn casting a long pale shadow shaped like a king across the navy band"/>
      </svg>
      <h1 class="title">
        <span class="title-lead">RISE AS</span>
        <span class="title-main">CAPTAIN</span>
      </h1>
      <p class="author">ORWEN DALQUIST</p>
    </article>
  </main>
</body>
</html>
```